Tamarack Hearth Partners Business Card

Looking for a new business card layout. We are a real estate firm w/ a logo, old design attached. Must keep the same elements on there, just need a fresh look and possible some foil accents. Looking for a simpler design w/ more modern style.

Target Market(s)

Real Estate clients

Industry/Entity Type

Real Estate Agent

Contact Information for Business Card

see attached

Font styles to use
Sans Serif

Requirements
Must have
• all elements on current biz card
Nice to have
• modern look, simpler than we have!
Should not have
• no serif fonts

```html
<!DOCTYPE html>
<html lang="en">
<head>
<meta charset="utf-8">
<title>Tamarack Hearth Partners – Business Card</title>
<link href="https://fonts.googleapis.com/css2?family=Poppins:wght@400;500;700;800&display=swap" rel="stylesheet">
<style>
  :root {
    --ink: #0b0b0b;
    --paper: #ffffff;
    --teal: #1fc6dc;
    --sky: #1a9fe0;
    --leaf: #8cc63f;
    --stage: #2a2a2c;
    --photo-light: #e9e6e1;
    --photo-mid: #d8c3a4;
    --photo-shirt: #2bc3c9;
  }
  * { box-sizing: border-box; margin: 0; padding: 0; }
  html, body { width: 1200px; height: 880px; overflow: hidden; }
  body {
    background: var(--stage);
    font-family: "Poppins", sans-serif;
    display: flex;
    flex-direction: column;
    align-items: center;
    justify-content: center;
    gap: 40px;
  }
  .card {
    width: 640px;
    height: 366px;
    border-radius: 22px;
    overflow: hidden;
    position: relative;
    box-shadow: 0 10px 30px rgba(0,0,0,.45);
  }

  /* Front */
  .card--front {
    background: var(--paper);
    display: flex;
    align-items: center;
    justify-content: center;
  }
  .brand-lockup {
    display: flex;
    align-items: center;
    gap: 16px;
  }
  .brand-lockup__square {
    width: 26px;
    height: 26px;
    background: var(--leaf);
  }
  .brand-lockup__name {
    font-weight: 800;
    font-size: 36px;
    color: var(--ink);
    letter-spacing: -0.5px;
  }

  /* Back */
  .card--back {
    background: var(--ink);
    display: flex;
  }
  .agent-photo {
    width: 44%;
    height: 100%;
    background: linear-gradient(170deg, var(--photo-light) 0%, var(--photo-mid) 55%, var(--photo-shirt) 92%);
  }
  .agent-details {
    flex: 1;
    padding: 30px 28px 26px 34px;
    color: var(--paper);
    display: flex;
    flex-direction: column;
  }
  .agent-details__firm {
    font-weight: 800;
    font-size: 22px;
    line-height: 1.1;
    color: var(--paper);
  }
  .agent-details__name {
    margin-top: 18px;
    font-weight: 700;
    font-size: 30px;
    line-height: 1;
  }
  .agent-details__title {
    margin-top: 4px;
    font-weight: 500;
    font-size: 15px;
    color: var(--teal);
  }
  .phone-list { margin-top: 14px; list-style: none; }
  .phone-list li {
    font-size: 26px;
    line-height: 1.15;
    font-weight: 400;
  }
  .phone-list .label {
    font-size: 14px;
    font-weight: 500;
    color: var(--teal);
    margin-right: 6px;
  }
  .web-links { margin-top: 12px; font-size: 15px; line-height: 1.35; }
  .web-links .site { color: var(--teal); }
  .office-address { margin-top: 10px; font-size: 14px; line-height: 1.35; font-style: normal; }
</style>
</head>
<body>

  <section class="card card--front">
    <div class="brand-lockup">
      <span class="brand-lockup__square"></span>
      <span class="brand-lockup__name">Tamarack Hearth Partners</span>
    </div>
  </section>

  <section class="card card--back">
    <div class="agent-photo" role="img" aria-label="Portrait photo of the broker in a teal top"></div>
    <div class="agent-details">
      <p class="agent-details__firm">Tamarack Hearth Partners</p>
      <p class="agent-details__name">Marin Ellery</p>
      <p class="agent-details__title">Principal Broker</p>
      <ul class="phone-list">
        <li><span class="label">Office:</span>555-201-7348</li>
        <li><span class="label">Cell:</span>555-309-6621</li>
      </ul>
      <p class="web-links">
        <span class="email">marin@hearthkeys.com</span><br>
        <span class="site">TamarackHearth-Homes.com</span>
      </p>
      <address class="office-address">
        418 NW Alder Ave.<br>
        Pinecrest, OR 97999
      </address>
    </div>
  </section>

</body>
</html>
```